Indian Lunch Delivery company needs a google ad banner for advertising its offering

We are a Kolkata, India based startup delivering lunch to office buildings in the city. We only serve set meals (vegetarian and non-vegetarian). Minimum order quantity is 5 boxes. The name of the brand is Brimvora (Thali=platter). Our USP-
We cook fresh
Trans-fat free
No emulsifiers, preservatives or artificial colorings used.
Importantly, we are a value for money brand. To be precise our meals costs just .99 c.
Target Market(s)
Young professionals
Industry/Entity Type
It Company
Font styles to use
Sans Serif
Requirements
Must have
- Home made food feel to it
Nice to have
- Lots of colours

```html
<!DOCTYPE html>
<html lang="en">
<head>
<meta charset="UTF-8">
<title>Brimvora – Lunch Banners</title>
<link href="https://fonts.googleapis.com/css2?family=Questrial&family=Montserrat:wght@700&display=swap" rel="stylesheet">
<style>
  :root {
    --coral: #e8735e;
    --coral-dark: #d9614c;
    --grey: #6a6a6a;
    --grey-dark: #555555;
    --panel-light: #f4f4f4;
    --panel-mid: #e2e2e2;
    --ink: #3d3d3d;
    --white: #ffffff;
    --page: #f2f2f2;
    --food-warm: #b8763a;
    --food-deep: #7a4a22;
    --food-light: #d9b27a;
  }
  * { margin: 0; padding: 0; box-sizing: border-box; }
  html, body { width: 1200px; height: 1200px; overflow: hidden; }
  body {
    background: var(--page);
    font-family: "Questrial", "Century Gothic", sans-serif;
    position: relative;
  }
  .banner { position: absolute; overflow: hidden;
    background: linear-gradient(180deg, var(--panel-light), var(--panel-mid)); }

  /* ---------- vertical banner ---------- */
  .banner--tall { left: 431px; top: 159px; width: 305px; height: 507px; }
  .tall-header { position: absolute; left: 0; top: 0; width: 305px; height: 196px; }
  .tall-header .word { position: absolute; left: 0; width: 305px; text-align: center; color: var(--white); line-height: 1; }
  .tall-header .w-freshly { top: 12px; font-size: 52px; }
  .tall-header .w-cooked { top: 74px; font-size: 46px; }
  .tall-header .w-transfat { top: 129px; font-size: 28px; }

  .benefits { position: absolute; list-style: none; color: var(--ink); }
  .benefits li { position: relative; padding-left: 22px; line-height: 1; }
  .benefits li::before { content: ""; position: absolute; left: 0; top: 50%;
    width: 10px; height: 10px; margin-top: -6px; border-radius: 50%; background: var(--coral); }
  .banner--tall .benefits { left: 40px; top: 206px; font-size: 20px; }
  .banner--tall .benefits li { margin-bottom: 8px; }

  .price-pill { position: absolute; background: var(--grey); border: 3px solid var(--coral);
    border-radius: 30px; color: var(--white); font-family: "Montserrat", sans-serif; font-weight: 700;
    text-align: center; line-height: 1.15; display: flex; align-items: center; justify-content: center; }
  .banner--tall .price-pill { left: 58px; top: 293px; width: 179px; height: 50px; font-size: 14px; }

  .min-order { position: absolute; color: var(--ink); white-space: nowrap; line-height: 1; }
  .banner--tall .min-order { left: 0; width: 305px; text-align: center; top: 355px; font-size: 15px; }

  .strip { position: absolute; display: flex; gap: 2px; }
  .banner--tall .strip { left: 0; top: 381px; width: 305px; height: 126px; border-top: 3px solid var(--grey); }

  .photo { height: 100%; }
  .photo--curry { background: radial-gradient(circle at 55% 65%, #c2452a 0 22%, var(--food-light) 40%, var(--food-warm) 75%, var(--food-deep)); }
  .photo--thali { background: radial-gradient(circle at 50% 55%, #b59a3a 0 25%, var(--food-warm) 55%, var(--food-deep)); }

  .brand-panel { background: var(--coral); height: 100%; position: relative; color: var(--white); text-align: center; }
  .brand-mark { position: absolute; left: 50%; border-radius: 50%; background: var(--grey);
    border: 3px solid var(--white); display: flex; align-items: center; justify-content: center;
    color: var(--white); }
  .contact { position: absolute; left: 0; width: 100%; line-height: 1.25; }

  .banner--tall .photo--curry { width: 104px; }
  .banner--tall .brand-panel { width: 95px; }
  .banner--tall .photo--thali { width: 100px; }
  .banner--tall .brand-mark { top: 8px; width: 80px; height: 80px; margin-left: -40px; font-size: 13px; }
  .banner--tall .contact { top: 95px; font-size: 9px; }

  /* ---------- horizontal banner ---------- */
  .banner--wide { left: 86px; top: 720px; width: 1033px; height: 200px; }
  .wide-ribbon { position: absolute; left: 41px; top: 0; width: 165px; height: 186px; }
  .wide-ribbon .word { position: absolute; left: 0; width: 165px; text-align: center; color: var(--white); line-height: 1; }
  .wide-ribbon .w-freshly { top: 22px; font-size: 30px; }
  .wide-ribbon .w-cooked { top: 50px; font-size: 28px; }
  .wide-ribbon .w-transfat { top: 89px; font-size: 22px; }
  .wide-ribbon .w-free { top: 110px; font-size: 52px; }

  .banner--wide .benefits { left: 233px; top: 18px; font-size: 24px; }
  .banner--wide .benefits li { margin-bottom: 5px; }
  .banner--wide .price-pill { left: 250px; top: 108px; width: 201px; height: 55px; font-size: 17px; }
  .banner--wide .min-order { left: 248px; top: 176px; font-size: 14px; }

  .banner--wide .strip { left: 505px; top: 0; width: 528px; height: 200px;
    border-left: 6px solid var(--grey); padding-left: 8px; background: var(--coral); gap: 0; }
  .banner--wide .photo--curry { width: 175px; margin-right: 5px; }
  .banner--wide .brand-panel { width: 166px; margin-right: 4px; }
  .banner--wide .photo--thali { width: 164px; }
  .banner--wide .brand-mark { top: 12px; width: 132px; height: 132px; margin-left: -66px; font-size: 19px; }
  .banner--wide .contact { top: 152px; font-size: 16px; }
</style>
</head>
<body>

<section class="banner banner--tall" aria-label="Vertical lunch banner">
  <div class="tall-header">
    <svg width="305" height="196" viewBox="0 0 305 196" aria-hidden="true">
      <polygon points="0,166 152,196 305,166 305,172 152,202 0,172" fill="var(--grey-dark)"/>
      <polygon points="0,0 305,0 305,166 152,191 0,166" fill="var(--coral)"/>
      <rect x="0" y="69" width="305" height="51" fill="var(--grey)"/>
    </svg>
    <div class="word w-freshly">FRESHLY</div>
    <div class="word w-cooked">COOKED</div>
    <div class="word w-transfat">TRANS-FAT FREE</div>
  </div>
  <ul class="benefits">
    <li>No Emulsifiers</li>
    <li>No Preservatives</li>
    <li>No Artificial colourings</li>
  </ul>
  <div class="price-pill">STARTING FROM<br>FROM 65/- ONLY</div>
  <p class="min-order">Minimum order quantity is 5 thalis</p>
  <div class="strip">
    <div class="photo photo--curry" role="img" aria-label="Photo of a bowl of curry with rice, naan and lime"></div>
    <div class="brand-panel">
      <div class="brand-mark">Brimvora</div>
      <p class="contact">Call: 9800012345<br>www.brimvora.com</p>
    </div>
    <div class="photo photo--thali" role="img" aria-label="Photo of a thali platter with small bowls of dishes"></div>
  </div>
</section>

<section class="banner banner--wide" aria-label="Horizontal lunch banner">
  <div class="wide-ribbon">
    <svg width="165" height="186" viewBox="0 0 165 186" aria-hidden="true">
      <polygon points="0,160 82,186 165,160 165,168 82,194 0,168" fill="var(--grey-dark)"/>
      <polygon points="0,0 165,0 165,160 82,180 0,160" fill="var(--coral)"/>
      <rect x="0" y="0" width="165" height="80" fill="var(--grey)"/>
    </svg>
    <div class="word w-freshly">FRESHLY</div>
    <div class="word w-cooked">COOKED</div>
    <div class="word w-transfat">TRANS-FAT</div>
    <div class="word w-free">FREE</div>
  </div>
  <ul class="benefits">
    <li>No Emulsifiers</li>
    <li>No Preservatives</li>
    <li>No Artificial colourings</li>
  </ul>
  <div class="price-pill">STARTING FROM<br>FROM 65/- ONLY</div>
  <p class="min-order">Minimum order quantity is 5 thalis</p>
  <div class="strip">
    <div class="photo photo--curry" role="img" aria-label="Photo of a bowl of curry with rice, naan and lime"></div>
    <div class="brand-panel">
      <div class="brand-mark">Brimvora</div>
      <p class="contact">Call: 9800012345<br>www.brimvora.com</p>
    </div>
    <div class="photo photo--thali" role="img" aria-label="Photo of a thali platter with small bowls of dishes"></div>
  </div>
</section>

</body>
</html>
```